Banner Pop Up Opt In Form REDESIGNS - SLEEK BLACK LOOK

Please redesign banners attached.

I am looking for a very sleek look....I do not like this collage of images on these current designs. Please keep all content same but use images that pop.

I have an acccount at www.pixmorrow-example.com or you can use your own images.

I like black background for somereason because it looks very sleek....but these designs should pop , build trust and credibility and have easy opt in form....SLEEK AND MODERN LOOK is what im looking for....

Target Market(s)

Consumers on websites

Requirements
Must have
• Please redesign banners attached.

Nice to have

Should not have

```html
<!DOCTYPE html>
<html lang="en">
<head>
<meta charset="utf-8">
<title>Enter to Win – Restaurant Certificate Opt In</title>
<link rel="stylesheet" href="https://fonts.googleapis.com/css2?family=Archivo:wght@400;500;700;800;900&display=swap">
<style>
  :root {
    --panel-black: #000000;
    --accent-orange: #f7941d;
    --text-white: #ffffff;
    --text-grey: #8f8f8f;
    --field-white: #ffffff;
    --field-line: #1a1a1a;
    --field-text: #111111;
    --note-grey: #a8a8a8;
    --frame-line: #3a3a3a;
  }
  * { box-sizing: border-box; margin: 0; padding: 0; }
  html, body {
    width: 1200px;
    height: 1030px;
    overflow: hidden;
    background: var(--panel-black);
  }
  .optin-banner {
    position: relative;
    width: 1200px;
    height: 1030px;
    background: var(--panel-black);
    font-family: "Archivo", "Helvetica Neue", Arial, sans-serif;
    overflow: hidden;
  }
  .banner-frame {
    position: absolute;
    inset: 22px 22px 22px 22px;
    border: 2px solid var(--frame-line);
    pointer-events: none;
    z-index: 2;
  }
  .offer-panel {
    position: absolute;
    left: 0;
    top: 0;
    width: 676px;
    height: 1030px;
    text-align: center;
  }
  .headline {
    position: absolute;
    left: 0;
    width: 650px;
    top: 70px;
    color: var(--accent-orange);
    font-weight: 800;
    font-size: 86px;
    line-height: 76px;
    letter-spacing: 1px;
    text-transform: uppercase;
  }
  .subscribe-line {
    position: absolute;
    left: 0;
    width: 650px;
    top: 282px;
    color: var(--text-grey);
    font-weight: 500;
    font-size: 27px;
    line-height: 40px;
    text-transform: uppercase;
  }
  .prize-amount {
    position: absolute;
    left: 0;
    width: 650px;
    top: 402px;
    color: var(--accent-orange);
    font-weight: 800;
    font-size: 88px;
    line-height: 90px;
  }
  .prize-name {
    position: absolute;
    left: 0;
    width: 650px;
    top: 494px;
    color: var(--text-white);
    font-weight: 800;
    font-size: 62px;
    line-height: 62px;
    text-transform: uppercase;
  }
  .signup-form {
    position: absolute;
    left: 40px;
    top: 681px;
    width: 606px;
  }
  .form-field {
    display: block;
    height: 74px;
    background: var(--field-white);
    border-bottom: 3px solid var(--field-line);
    padding-left: 22px;
    color: var(--field-text);
    font-size: 33px;
    font-weight: 500;
    line-height: 74px;
    text-align: left;
    text-transform: uppercase;
  }
  .form-footer {
    position: absolute;
    left: 40px;
    top: 909px;
    width: 606px;
    height: 80px;
  }
  .consent-note {
    position: absolute;
    left: 18px;
    top: 10px;
    width: 400px;
    color: var(--note-grey);
    font-size: 15px;
    line-height: 20px;
    text-align: left;
  }
  .submit-button {
    position: absolute;
    right: 0;
    top: 0;
    width: 196px;
    height: 80px;
    background: var(--accent-orange);
    color: var(--panel-black);
    font-family: "Archivo", "Helvetica Neue", Arial, sans-serif;
    font-weight: 800;
    font-size: 32px;
    border: none;
    text-transform: uppercase;
  }
  .dining-photo {
    position: absolute;
    left: 676px;
    top: 0;
    width: 524px;
    height: 1030px;
    background:
      radial-gradient(ellipse at 45% 22%, #d9b59a 0%, rgba(217,181,154,0) 38%),
      radial-gradient(ellipse at 40% 75%, #f0ece6 0%, rgba(240,236,230,0) 40%),
      radial-gradient(ellipse at 80% 55%, #6e5a3e 0%, rgba(110,90,62,0) 45%),
      linear-gradient(180deg, #c7a88a 0%, #b98b6d 30%, #8e6a4c 55%, #a08670 80%, #6a4a36 100%);
  }
</style>
</head>
<body>
  <div class="optin-banner">
    <section class="offer-panel">
      <h1 class="headline">Enter<br>To Win</h1>
      <p class="subscribe-line">Subscribe to our newsletter<br>and recieve a complimentary</p>
      <p class="prize-amount">$300</p>
      <p class="prize-name">Restaurant<br>Certificate</p>
      <form class="signup-form">
        <span class="form-field">Name</span>
        <span class="form-field">Email</span>
        <span class="form-field">Phone</span>
      </form>
      <div class="form-footer">
        <p class="consent-note">We will send an email and text message with the offer and instructions on how to redeem.</p>
        <button class="submit-button" type="button">Submit</button>
      </div>
    </section>
    <div class="dining-photo" role="img" aria-label="Photo of a smiling man at a restaurant table being served a plate of pasta, with wine glasses and dishes in the foreground"></div>
    <div class="banner-frame"></div>
  </div>
</body>
</html>
```